Three Fold Flyer

The purpose of this flyer is to provide customers with a quick view of what services we provide. The name of the company if Gentle Mirrorworks, we will be uploading our logo later today.

We would like the flyer to tell a story. Our customers should be with us through several of their life experiences, such as engagement, pregnancy, first child, second child, and the experience grows as their children join dance or sports teams, and later on their children will grow and the cycle will continue. We create life casting pieces that forever stay with these people and remind them of a special time and place. Our keepsakes can be displayed in shadow boxes, or mounted on boards and or stone.
We would love for the flyer to reflect a story line, about the moments we are capturing, it should have a emotional connection for people to want to have this special piece created for them. We were thinking that you may even want to connect the pictures and a small paragraph for each of the photos to explain what its about.
Updates

Project Deadline Extended
Reason: Would like to provide more time to designers to create just what we need. Thank you.

The flyer design should concentrate on a successful woman/couple running a business from home. Images of timeless keepsakes is the product. She can stay home with kids and still make an income by providing a creative service.
Hope this helps further in the design.

Target Market(s)

Emotional piece, that entices people to want to be part of this moment and really hits home. Audience is couples, families, moms, grandmothers and a like. The targeted celebrated moments are Engagement, pregnancy, birth of a child, gifts for Grandmothers, and Parents, celebrating family, ballet students etc. We really like the background of the flyer to be an elegant texture.

Industry/Entity Type

It Company

Requirements
Must have
• It must have a light elegant textured background.
Must be a three fold in landscape layout.
Appealing to families with lots of emotional feel
Nice to have
• The images included here, should be included where possible. The variety being offered must be exhibited.

There should be a flow from the first page on.
Life events such as
- engagement/wedding
-pregnancy
-new born
-christening
-ballerina
-family
Life events: golfers trophy, hockey,
Should not have
• For reference only: Please view the existing website for this service
www.harborlanemoldcraft.example
We are re-branding under Gentle Mirrorworks and want a different feel.

For logo colors, referr to
:the light blue colour is CMYK 41/33/14/0
the dark blue is CMYK 87/67/25/8

```html
<!DOCTYPE html>
<html lang="en">
<head>
<meta charset="utf-8">
<title>Gentle Mirrorworks – Tri-fold Flyer</title>
<link href="https://fonts.googleapis.com/css2?family=Tinos:wght@400;700&family=Cinzel:wght@400&family=Arimo:wght@400;700&display=swap" rel="stylesheet">
<style>
:root{
  --stage:#ebe8e3;
  --slate-top:#4a5566;
  --slate-bottom:#2c3442;
  --navy:#3b5a93;
  --lavender:#a8aecf;
  --lavender-light:#bcc1dc;
  --ink:#1d2230;
  --white:#ffffff;
  --frame:#1a1a1a;
}
*{box-sizing:border-box;margin:0;padding:0}
html,body{width:801px;height:1200px;overflow:hidden}
body{background:var(--stage);position:relative;font-family:"Tinos",serif;color:var(--ink)}
.sheet{position:absolute;left:75px;width:662px;height:510px;overflow:hidden;box-shadow:0 2px 8px rgba(0,0,0,.25)}
.sheet--outside{top:83px}
.sheet--inside{top:623px;background:var(--lavender)}
.panel{position:absolute;top:0;height:510px;overflow:hidden}
.photo{position:absolute;display:block}

/* outside */
.cover{left:0;width:220px;background:linear-gradient(180deg,var(--slate-top),var(--slate-bottom))}
.cover .photo{left:0;top:0;width:220px;height:150px;background:linear-gradient(160deg,#6d7684,#c9ccd2 55%,#3f4856)}
.cover__copy{position:absolute;left:10px;top:145px;width:188px;color:var(--white);font-size:8.6px;line-height:1.1}
.cover__title{font-size:12.6px;font-weight:700;line-height:1.15;margin-bottom:10px}
.cover__lead{font-weight:700;margin-bottom:10px}
.cover__closing{font-weight:700;margin-top:10px}
.contact-panel{left:220px;width:221px;background:var(--navy)}
.contact-panel .photo{left:0;top:0;width:221px;height:305px;background:linear-gradient(180deg,#e8e8e8,#8f8f8f 55%,#4a4a4a)}
.mission-panel{left:441px;width:221px;background:var(--navy)}
.mission-panel .photo{left:0;top:0;width:221px;height:305px;background:linear-gradient(160deg,#8a8f6c,#d9c9b8 45%,#6f5a4c)}
.wave{position:absolute;left:0;top:280px;width:221px;height:40px}
.brand{position:absolute;display:flex;align-items:center;gap:5px;color:var(--white);font-family:"Tinos",serif;font-weight:700;font-size:12px;white-space:nowrap}
.brand__dot{width:10px;height:10px;border-radius:50%;background:var(--lavender-light);flex:none}
.contact-panel .brand{left:58px;top:362px}
.mission-panel .brand{left:58px;top:440px;font-size:13px}
.contact{position:absolute;left:0;top:414px;width:221px;text-align:center;color:var(--white);font-size:9.6px;line-height:1.22;font-style:normal}
.contact__name{font-weight:700}
.mission{position:absolute;left:8px;top:311px;width:205px;text-align:center;color:var(--white);font-family:"Cinzel",serif;font-size:9.4px;line-height:1.25;letter-spacing:.02em}

/* inside */
.body{font-size:8.6px;line-height:8.8px;text-align:justify}
.body h3{font-size:8.6px;font-weight:700}
.intro{left:0;width:221px;background:var(--lavender)}
.intro .body{position:absolute;left:10px;top:20px;width:190px}
.frame-float{float:right;width:126px;height:64px;margin:2px 0 3px 5px;background:linear-gradient(90deg,#111,#777 30%,#9a8070 50%,#777 70%,#111);border:3px solid var(--frame)}
.benefits{position:absolute;left:0;top:306px;width:221px}
.benefits .photo--frame{left:0;top:0;width:108px;height:70px;background:linear-gradient(90deg,#111,#888 30%,#bbb 50%,#888 70%,#111);border:3px solid var(--frame)}
.benefits__head{position:absolute;left:112px;top:4px;width:104px;font-size:8.6px;font-weight:700;line-height:1.1}
.benefits ul{list-style:none;font-size:8.6px;line-height:1.12}
.benefits ul li::before{content:"•";margin-right:4px}
.benefits__short{position:absolute;left:116px;top:37px;width:104px}
.benefits__long{position:absolute;left:28px;top:86px;width:190px}
.opportunity{left:221px;width:220px;background:var(--lavender)}
.opportunity .body{position:absolute;left:24px;top:20px;width:188px}
.bio{position:absolute;left:0;top:262px;width:220px;height:248px;background:var(--navy)}
.bio .photo{left:24px;top:4px;width:61px;height:76px;background:linear-gradient(180deg,#d8d8d8,#6c6c6c);border:2px solid #ddd}
.bio__text{position:absolute;left:24px;top:8px;width:190px;color:var(--white);font-family:"Arimo",sans-serif;font-size:6.7px;line-height:1.12}
.bio__float{float:left;width:70px;height:76px}
.workshops{left:441px;width:221px;background:var(--lavender)}
.workshops__band{position:absolute;left:0;top:0;width:221px;height:50px;background:var(--navy)}
.workshops__title{position:absolute;left:0;top:12px;width:221px;text-align:center;color:var(--white);font-family:"Cinzel",serif;font-size:19px;font-weight:400;letter-spacing:.04em}
.workshops .body{position:absolute;left:24px;top:62px;width:190px;font-size:8.4px}
.workshops .body h3{font-size:8.4px}
.hands-float{float:right;width:100px;height:80px;margin:-24px -7px 2px 4px;background:radial-gradient(ellipse at 50% 45%,#f4f4f4,#c9ccd8 70%,var(--lavender))}
.spaced{letter-spacing:.28em;text-align:left}
.gap{margin-top:9px}
.workshops .photo--wedding{left:20px;top:405px;width:201px;height:105px;background:linear-gradient(150deg,#3d3a38,#6f6a63 40%,#d8cfc4 75%,#a78d7a)}
</style>
</head>
<body>

<section class="sheet sheet--outside">
  <article class="panel cover">
    <div class="photo" role="img" aria-label="Plaster cast of clasped hands, softly lit"></div>
    <div class="cover__copy">
      <h1 class="cover__title">Northbrook Studio<br>is looking to train YOU in the art of LifeCasting.</h1>
      <p class="cover__lead">Train with the best and most experienced in the business of LifeCasting. Create heirlooms and timeless treasures to capture your heart.</p>
      <p>Are you looking for a Home Based Business that offers flexibility, convenience, and creativity?</p>
      <p>Become a NB Associate through our Three Day Workshop and achieve financial freedom through the Art of LifeCasting Sculptures.</p>
      <p>Learn to create detailed impressions of babies hands and feet and create heirlooms set in professionally framed shadow boxes.</p>
      <p>Nurture your family and create a business controlled completely by You. Provide a service that satisfies your creative outlet while creating financial freedom.</p>
      <p>Become a NB Associate and receive your certification training through international lifecasting artist Helena Marsh and the Northern Casting Guild. There are no franchise fees, sales royalties or territory restrictions, simply a series of training and business support services designed to help you each step of the way!</p>
      <p class="cover__closing">We train entrepreneurial mom's Internationally. North America, Europe and beyond are open territories for NB Associates. Be the first to provide a service that will please many family's in your area.</p>
    </div>
  </article>

  <article class="panel contact-panel">
    <div class="photo" role="img" aria-label="Black and white photo of a parent holding a baby beside a cast of baby hands"></div>
    <svg class="wave" viewBox="0 0 221 40" aria-hidden="true"><path d="M0 40 V22 Q110 -4 221 18 V40 Z" fill="#3b5a93"/><path d="M0 22 Q110 -4 221 18" fill="none" stroke="#bcc1dc" stroke-width="3"/></svg>
    <div class="brand"><span class="brand__dot"></span>Gentle Mirrorworks</div>
    <address class="contact">
      <div class="contact__name">Helena Marsh</div>
      42 Willow Row, Fernbridge On. K0A 1X0<br>
      Telephone: 905-555-0148<br>
      Email: info@gentlemirrorworks.example
    </address>
  </article>

  <article class="panel mission-panel">
    <div class="photo" role="img" aria-label="Mother working on a laptop at home with her baby beside her"></div>
    <svg class="wave" viewBox="0 0 221 40" aria-hidden="true"><path d="M0 40 V18 Q110 -4 221 22 V40 Z" fill="#3b5a93"/><path d="M0 18 Q110 -4 221 22" fill="none" stroke="#bcc1dc" stroke-width="3"/></svg>
    <p class="mission">"To empower and educate through innovation and the creative process.<br>To be a leader in the industry of life casting through its associates."</p>
    <div class="brand"><span class="brand__dot"></span>Gentle Mirrorworks</div>
  </article>
</section>

<section class="sheet sheet--inside">
  <article class="panel intro">
    <div class="body">
      <h3>What is LifeCasting?</h3>
      <p>LifeCasting is the process of taking an impression of a human form. Skin safe molding material called "alginate" is a prosthetic grade hypoallergenic compound used to create detailed impressions of children's feet and hands. The powder is a composition of several <span class="frame-float" role="img" aria-label="Shadow box frame with baby hand and foot casts and a photo"></span>materials including sea weed and clay. Completely hypoallergenic and safe to skin, detail and strength of the alginate is key to creating the highest quality work.</p>
      <p>Sculptural images displayed creatively, will determine the standards for creating personal heirlooms. Molding the human form is an ancient art dating back to the Egyptians and made popular in Victorian times.</p>
      <p>There is a huge demand for creative entrepreneurs in life casting. This new service is still in its infancy and will bring joy to many moms, dads, grandparents and loved ones. Mastering the technique will provide unique opportunities for castings. Artistry is an asset but not essential.</p>
    </div>
    <div class="benefits">
      <div class="photo photo--frame" role="img" aria-label="Framed set of three baby hand and foot casts"></div>
      <div class="benefits__head">Benefits of a home based business from NB Studios</div>
      <ul class="benefits__short"><li>Small Start Up Investment</li><li>Small Inventory</li><li>Controlling your working hours</li></ul>
      <ul class="benefits__long">
        <li>Have more time with family</li><li>No office politics</li><li>Gain a Supportive network</li><li>Enjoy helping others</li><li>A sense of purpose about your work</li><li>Creative Fulfillment</li><li>Environmentally Friendly Product</li><li>Extra income</li><li>Potential for growth</li>
      </ul>
    </div>
  </article>

  <article class="panel opportunity">
    <div class="body">
      <h3>The Opportunity<br>Baby Hand and Foot Castings</h3>
      <p>Casting services are desperately needed everywhere.</p>
      <p>NB LifeCasting Studio receives emails from the U. S. and Canada requesting casting services.</p>
      <p>The Baby Casting Service sells itself and the best part is, natural artistic abilities are not required in order to learn the techniques.</p>
      <p>Throughout my 15 years in the business, I've managed to simplify the process for you. Acquired color changing molding material to make it simple for all my Associates to master. If you enjoy working with people and would like to provide a meaningful and very unique service that will touch lives for generations to come, consider a career in life casting.</p>
      <p>With NB LifeCasting, you are offered full training that includes all necessary information to set up a Home Based Business for a fraction of the cost. Market your business based on the time you can devote to managing family and work. Choose your kitchen or spare room – a table and a few supplies will provide the necessary elements to set up your business while determining your own schedule.</p>
    </div>
    <div class="bio">
      <div class="photo" role="img" aria-label="Portrait of the studio founder"></div>
      <p class="bio__text"><span class="bio__float"></span><b>Helena Marsh</b> has been an artist in various mediums for over 25 years. Trained as a sculptor working in clay, she has lived, worked, and taught throughout the U. S. and Canada. As a life casting artist in N.Y. Helena has worked with sport celebrities such as boxing great Rocco Vance, Tom Braddock, Leon Pryce and Victor Halden. A commission to create a sculpture of Rocco Vance began a career in LifeCasting. Once the sculpture (bust) was complete, Helena cast Mr. Vance's fists as a memento and tribute to his talent in the ring (Iron Ring film). This was to be the start of a new career. On returning to the Toronto area, Helena's reputation grew as the premier life casting artist for shows and private commissions. T.V and radio appearances, several news papers, and magazines have showcased her work. Helena has combined her sculptural background with her LifeCasting skills to provide her clients with exceptional works of art.</p>
    </div>
  </article>

  <article class="panel workshops">
    <div class="workshops__band"></div>
    <h2 class="workshops__title">WORKSHOPS</h2>
    <div class="body">
      <span class="hands-float" role="img" aria-label="White cast of a couple's joined hands"></span>
      <h3 class="spaced">Home based business workshop</h3>
      <p class="spaced">There are no Franchise Fees, Sales Royalties or Territory</p>
      <p>Restrictions, simply a series of Training and Business Support Services designed to help you each step of the way!</p>
      <h3 class="gap">Belly Castings - full day workshop</h3>
      <p>Prenatal casting for mom's to be. Take detailed impressions and include mom, dad and siblings in this very personal format.</p>
      <p>Sculptures mounted on a base or hung on a wall will provide your clients with additional heirloom sculptures.</p>
      <p>Your client base will increase and you broaden your financial opportunities.</p>
      <h3 class="gap">Ballerina - Engagement - Golfers Trophy - full day workshop</h3>
      <p>Create a client base in all areas or specialize.</p>
      <p>These three styles alone will broaden your base of possibilities.</p>
      <p>They are more complex castings and need additional time to develop.</p>
      <p>However, you will be able to include a wider audience and offer more to potential clients.</p>
      <p>Both days will cover demonstrations to completion and provide a Detailed Manual to support your workshop.</p>
    </div>
    <div class="photo photo--wedding" role="img" aria-label="Framed wedding photo beside a cast of hands with rings"></div>
  </article>
</section>

</body>
</html>
```